Business card for Industrial Automation Company.

The company is called Process and Signal Dynamics. We are a systems integration company in South Africa specializing in PLC and SCADA programming, systems integration and industrial automation. Attached find logo and cover letter of the company for a feel of the general look. The website is still under development, so you will have to use your own ideas.

Please blend the colors on the business card as per the logo colors. Must be clean, professional look. Please submit a creative professional design. If a background color is used please do not use dark colored backgrounds.

Target Market(s)

Mining

Industry/Entity Type

Engineering Consultant

Contact Information for Business Card

Gerrit van Dyk (NDip Instrumentation; BEng)
Principal / Controls Engineer

Postal Address
PO Box 2867
Vredenburg
7380

Physical Address:
Kloofhoek Street 27
Vredenburg
7380

Tel: +22 548 6170
Cell: +27 82 953 4086
Mail: gerritv@psd-zx.com
Web: www.psd-zx.com

Font styles to use
Sans Serif

Colors

Designer to choose colors to be used in the design.

Requirements
Must have
• Backside of the card must also contain the following:
• Services
• *Industrial Automation
• *Control System design and configuration
• *Systems Integration
• *Equipment Supply
• Industries
• *Mining
• *Factory
• *Oil and Gas
Nice to have
• Colors must blend in with colors of logo. Not too much color and no dark backgrounds.
Should not have
• dark / black background. Preferably white / light background if any.

```html
<!DOCTYPE html>
<html lang="en">
<head>
<meta charset="utf-8">
<title>Process and Signal Dynamics — Business Card</title>
<link rel="stylesheet" href="https://fonts.googleapis.com/css2?family=Open+Sans:wght@400;600;700&family=Roboto+Slab:wght@400&display=swap">
<style>
  :root {
    --brand-blue: #1d4580;
    --accent-lime: #d3df24;
    --paper: #ffffff;
    --backdrop: #d9d9d9;
    --ink-grey: #5a5a5a;
    --ink-dark: #333333;
  }
  * { box-sizing: border-box; margin: 0; padding: 0; }
  html, body {
    width: 1200px; height: 800px; overflow: hidden;
    background: var(--backdrop);
    font-family: "Open Sans", Arial, sans-serif;
  }
  .sheet {
    width: 1200px; height: 800px;
    display: flex; flex-direction: column; align-items: center; justify-content: center;
    gap: 36px;
  }
  .card {
    position: relative;
    width: 600px; height: 343px;
    background: var(--paper);
    box-shadow: 0 6px 18px rgba(0,0,0,0.18);
    overflow: hidden;
  }
  .band {
    position: absolute; left: 0; right: 0; bottom: 0;
    background: var(--brand-blue);
    color: var(--paper);
  }

  /* Back side */
  .card-back .band { height: 150px; }
  .card-back .edge-accent {
    position: absolute; right: 0; top: 0; bottom: 0; width: 4px; background: var(--accent-lime);
  }
  .brand {
    position: absolute; left: 0; right: 0; top: 62px;
    display: flex; flex-direction: column; align-items: center; gap: 8px;
  }
  .brand-lockup { display: flex; align-items: center; gap: 12px; }
  .brand-dot {
    width: 26px; height: 26px; border-radius: 50%; background: var(--brand-blue);
  }
  .brand-name {
    font-weight: 700; font-size: 30px; color: var(--brand-blue); letter-spacing: -0.3px;
  }
  .brand-tagline {
    font-size: 13px; color: var(--ink-grey); letter-spacing: 1px;
  }
  .services-rule {
    position: absolute; left: 24px; right: 24px; top: 22px;
    display: flex; align-items: center; gap: 10px;
  }
  .services-rule::before, .services-rule::after {
    content: ""; flex: 1; height: 1px; background: var(--accent-lime);
  }
  .services-title { color: var(--accent-lime); font-size: 14px; font-weight: 600; }
  .service-columns {
    position: absolute; left: 24px; right: 24px; top: 58px;
    display: flex; align-items: center; justify-content: space-between;
  }
  .service-item { font-size: 12.5px; line-height: 1.4; }
  .divider { width: 1px; height: 30px; background: rgba(255,255,255,0.85); }

  /* Front side */
  .card-front .band { height: 166px; }
  .holder {
    position: absolute; left: 40px; right: 40px; top: 52px;
  }
  .holder-line { display: flex; align-items: baseline; gap: 8px; justify-content: center; }
  .holder-name {
    font-family: "Roboto Slab", Georgia, serif; font-weight: 400; font-size: 38px; color: var(--brand-blue);
  }
  .holder-credentials { font-size: 13px; color: var(--ink-dark); }
  .holder-rule {
    margin-top: 6px; display: flex; align-items: center; gap: 10px;
  }
  .holder-rule::before, .holder-rule::after { content: ""; flex: 1; height: 1px; background: #444; }
  .holder-title { font-size: 13px; color: var(--ink-dark); font-weight: 600; }
  .contact-columns {
    position: absolute; left: 30px; right: 30px; top: 46px;
    display: flex; justify-content: space-between;
  }
  .contact-label { color: var(--accent-lime); font-size: 12.5px; font-weight: 600; margin-bottom: 4px; }
  .contact-value { font-size: 12px; line-height: 1.45; }
</style>
</head>
<body>
<main class="sheet">

  <section class="card card-back" aria-label="Card back">
    <div class="brand">
      <div class="brand-lockup">
        <span class="brand-dot"></span>
        <span class="brand-name">Process and Signal Dynamics</span>
      </div>
      <p class="brand-tagline">Engineering dependable control daily!</p>
    </div>
    <div class="band">
      <div class="services-rule"><span class="services-title">Services</span></div>
      <div class="service-columns">
        <p class="service-item">Industrial Automation<br>Control System design &amp;<br>configuration</p>
        <span class="divider"></span>
        <p class="service-item">Systems Integration<br>Equipment Supply</p>
        <span class="divider"></span>
        <p class="service-item">Industries<br>Mining</p>
        <span class="divider"></span>
        <p class="service-item">Factory<br>Oil and Gas</p>
      </div>
    </div>
    <span class="edge-accent"></span>
  </section>

  <section class="card card-front" aria-label="Card front">
    <div class="holder">
      <div class="holder-line">
        <h1 class="holder-name">Gerrit van Dyk</h1>
        <span class="holder-credentials">(NDip Instrumentation; BEng)</span>
      </div>
      <div class="holder-rule"><span class="holder-title">Principal / Controls Engineer</span></div>
    </div>
    <div class="band">
      <div class="contact-columns">
        <div class="contact-block">
          <p class="contact-label">Postal Address</p>
          <p class="contact-value">PO Box 2867<br>Kransdal 7412</p>
        </div>
        <div class="contact-block">
          <p class="contact-label">Physical Address</p>
          <p class="contact-value">Kloofhoek Street 27<br>Kransdal 7412</p>
        </div>
        <div class="contact-block">
          <p class="contact-label">Phone/Cell</p>
          <p class="contact-value">Tel: +22 548 6170<br>Cell: +27 82 953 4086</p>
        </div>
        <div class="contact-block">
          <p class="contact-label">Web/Email</p>
          <p class="contact-value">Mail: gerritv@psd-zx.com<br>Web: www.psd-zx.com</p>
        </div>
      </div>
    </div>
  </section>

</main>
</body>
</html>
```